会社パンフレットリニューアルにあたり、デザインを依頼させていただきます。(1)ポケットフォルダー(方ポケット、名刺)、(2)その中に入れて使うA4片面6枚(1枚ずつリーフとして使います)の会社案内デザインをお願いします。カラーはブルーベースで、デザインもシンプルかつ高級感・インテリジェンス感のあるものを求めます。
A4
6ページ
• 高解像度JPG (.jpg)
• イラストレーター形式 (.ai)
【参考】企業サイト: http://www.kmvtr.com/
以前のコンペのミネギさんのポケットホルダーデザイン(http://www.pivora.jp/work/proposal/731926)で選ばれた案が素敵だと思いました。色は弊社の求めるものと違いますが。
一箇所誤字がありました。訂正させていただきます。失礼しました。
×方ポケット
○片ポケット
です。
何度も恐れいります。
×ポケットフォルダー(方ポケット、名刺)
○ポケットフォルダー(片ポケット、名刺1枚差込みあり)
でした。
みなさまご提案ありがとうございました!
これより社内で検討させていただきます。しばらくお待ちください。

今回の主要な選定理由は3つあります。
1.さまざまなクライアントに対してお渡しできる嫌味のないシンプルさ・清潔さ持ったデザインを選定させていただきました。

2.ポケットフォルダーだけではなく、差込資料の方のデザインも同様に重要な
ため、最初から差込資料デザイン案をすべて出していただいた方を選考時に優先させていただきました。

3.弊社社内調整に時間をいただいたり、修正をお願いすることが予想されたため、やりとりについて誠意を持って取り組んでいただけそうな方にお願いした次第です。

皆様、すばらしいご提案をありがとうございました!

Pivoraの利用が初めてで、すばらしいご提案を
これほどたくさんいただけるものとは思っておりませんでした。
感謝しております。またどうぞよろしくお願いいたします。

```html
<!DOCTYPE html>
<html lang="ja">
<head>
<meta charset="utf-8">
<title>会社概要 1</title>
<link href="https://fonts.googleapis.com/css2?family=Noto+Sans+JP:wght@400;500;700&display=swap" rel="stylesheet">
<style>
  :root {
    --brand-blue: #1f7fc4;
    --deep-blue: #17589a;
    --sky: #bfe0f4;
    --ink: #333;
    --rule: #b9cfe0;
    --label-bg: #e4eff8;
    --paper: #ffffff;
  }
  * { margin: 0; padding: 0; box-sizing: border-box; }
  html, body { width: 848px; height: 1200px; overflow: hidden; background: var(--paper); }
  body { font-family: "Noto Sans JP", sans-serif; color: var(--ink); }
  .page { position: relative; width: 848px; height: 1200px; overflow: hidden; background: var(--paper); }

  .company-mark { position: absolute; top: 14px; right: 96px; font-size: 9px; color: #777; }

  .headline {
    position: absolute; left: 64px; top: 34px;
    font-size: 27px; font-weight: 700; line-height: 1.55; color: var(--brand-blue);
    letter-spacing: 0.02em;
  }

  .section-tab {
    position: absolute; top: 0; right: 0; width: 78px; height: 290px;
    display: flex; flex-direction: column; align-items: center;
  }
  .section-tab .label {
    margin-top: 40px; writing-mode: vertical-rl; font-size: 12px; color: #fff;
    background: var(--brand-blue); padding: 8px 4px; letter-spacing: 0.2em;
  }
  .section-tab .number {
    font-size: 78px; font-weight: 700; color: var(--brand-blue); line-height: 1; margin-top: 8px;
  }
  .section-tab .brand {
    margin-top: 10px; font-size: 22px; font-weight: 700; color: var(--brand-blue);
  }

  .earth-backdrop {
    position: absolute; left: 0; top: 150px; width: 770px; height: 620px;
    background:
      radial-gradient(ellipse 120% 60% at 50% 105%, #2c6fae 0%, #5e9fd2 35%, transparent 60%),
      linear-gradient(180deg, #ffffff 0%, #e6f3fb 30%, var(--sky) 65%, #7fb6df 100%);
  }

  .service-diagram { position: absolute; left: 130px; top: 150px; }

  .profile-table {
    position: absolute; left: 100px; top: 790px; width: 536px;
    border-collapse: collapse; font-size: 10.5px; line-height: 1.5;
  }
  .profile-table th, .profile-table td {
    border-bottom: 1px solid var(--rule); padding: 3px 8px; vertical-align: top; text-align: left;
  }
  .profile-table th { width: 150px; background: var(--label-bg); font-weight: 500; color: var(--deep-blue); }

  .photo-slot {
    position: absolute; left: 650px; top: 790px; width: 170px; height: 220px;
    background: linear-gradient(160deg, #dfe9f2, #b8cadb);
  }
  .photo-slot span { position: absolute; left: 8px; top: 6px; font-size: 9px; color: #6a7d90; }

  .footer { position: absolute; left: 84px; top: 1140px; display: flex; align-items: center; gap: 12px; }
  .footer .badge { width: 40px; height: 40px; border-radius: 50%; border: 2px solid var(--brand-blue); }
  .footer p { font-size: 8px; color: #666; line-height: 1.5; width: 440px; }
</style>
</head>
<body>
<div class="page">
  <div class="company-mark">株式会社ケイ・エム・ヴイ</div>

  <h1 class="headline">
    語学プロフェッショナルとして長年、<br>
    業界を牽引してきた実績があります。<br>
    多くのお客様から信頼と支持をいただいている<br>
    KMVのサービス・クオリティをぜひお試しください。
  </h1>

  <aside class="section-tab">
    <div class="label">会社概要</div>
    <div class="number">1</div>
    <div class="brand">KMV</div>
  </aside>

  <div class="earth-backdrop" role="img" aria-label="青い空と地球の写真"></div>

  <svg class="service-diagram" width="580" height="610" viewBox="0 0 580 610" font-family="Noto Sans JP, sans-serif">
    <g opacity="0.82">
      <circle cx="295" cy="175" r="127" fill="#f6a21c"/>
      <circle cx="153" cy="294" r="127" fill="#ec6f9a"/>
      <circle cx="433" cy="294" r="127" fill="#8cc63e"/>
      <circle cx="295" cy="432" r="127" fill="#2f8fd6"/>
    </g>
    <circle cx="289" cy="289" r="90" fill="#fff"/>
    <g fill="#fff" font-weight="700" font-size="18" text-anchor="middle">
      <text x="295" y="148">MICE</text>
      <text x="140" y="300">通訳</text>
      <text x="440" y="300">翻訳</text>
      <text x="295" y="448">人材派遣</text>
    </g>
    <g fill="#444" font-weight="700" font-size="17" text-anchor="middle">
      <text x="289" y="268">語学</text>
      <text x="289" y="292">プロフェッショナル</text>
      <text x="289" y="316">サービス</text>
    </g>
  </svg>

  <table class="profile-table">
    <tr><th>商号</th><td>株式会社ケイ・エム・ヴイ（英語名 KMV Inc.）</td></tr>
    <tr><th>本社所在地・連絡先</th><td>〒100-0000 東京都千代田区架空町1-2-3 サンプルビル5F</td></tr>
    <tr><th>TEL</th><td>03-0000-4821</td></tr>
    <tr><th>URL</th><td>http://www.kmvtr.com/</td></tr>
    <tr><th>資本金</th><td>5,000万円</td></tr>
    <tr><th>代表取締役社長</th><td>山野 一郎</td></tr>
    <tr><th>主要取引銀行</th><td>青葉中央銀行　本店<br>東都共栄銀行　中央支店<br>湊川信託銀行　丸の内支店</td></tr>
    <tr><th>労働者派遣事業許可番号</th><td>派13-000000<br>有料職業紹介 13-ユ-000000</td></tr>
    <tr><th>事業内容</th><td>通訳、翻訳、MICE（国際会議・イベント）の企画・運営、人材派遣</td></tr>
    <tr><th>グループ企業</th><td>株式会社ケイ・エム・ヴイ・コンサルティング<br>株式会社ケイ・エム・ヴイ・アカデミー</td></tr>
  </table>

  <div class="photo-slot" role="img" aria-label="本社ビルの外観写真"><span>外観写真</span></div>

  <footer class="footer">
    <div class="badge"></div>
    <p>当社は個人情報保護の認証を取得しています。お客様の情報は適切な管理のもと、厳重に取り扱っております。</p>
  </footer>
</div>
</body>
</html>
```